"Landing Page Design for Premium Eco-Friendly Laundry Strips – Plooifris.nl"

We need a visually appealing and high-converting landing page for our premium laundry strips, emphasizing luxury, sustainability, and ease of use. The page should include sections such as:

Hero Section: A compelling introduction with a strong headline, subheadline, and a clear call-to-action (CTA).
Product Benefits: Highlighting key features like eco-friendliness, long-lasting scent, and hypoallergenic qualities.
Product Description: Focusing on innovation and sustainability.
How It Works: Simple, visual steps for using the product.
Customer Reviews: Authentic testimonials to build trust and social proof.
FAQ Section: Addressing common concerns about the product.
The design should maintain a luxurious aesthetic while ensuring clarity and user-friendliness. We also offer free shipping on all orders, a key differentiator to be prominently displayed. All texts and translations are already provided for implementation. Please deliver the design in Figma format."

Target Market(s)

"Eco-conscious consumers and families seeking premium and sustainable laundry solutions. Target age group: 25-50, predominantly women who prioritize luxury and environmental impact."

Industry/Entity Type

"Laundry care and eco-friendly consumer goods."

Coding

Requirements
Must have
• A visually luxurious design emphasizing premium quality and eco-friendliness. Clear call-to-actions (e.g., 'Try Now – Free Shipping'). Sections for product benefits, how it works, customer reviews, and FAQ. Highlight free shipping with no minimum order prominently."
Nice to have
• Elegant, minimalist animations to enhance the premium feel. Subtle use of gold and black to emphasize luxury, with a touch of green for sustainability. Interactive customer reviews section (e.g., carousel or testimonials)."
Should not have
• Overly cluttered designs or overwhelming text blocks. Generic stock photos not aligned with our brand identity. Bright or overly playful color schemes that detract from the premium feel."

```html
<!DOCTYPE html>
<html lang="nl">
<head>
<meta charset="utf-8">
<title>Plooifris – Premium Wasstrips</title>
<link href="https://fonts.googleapis.com/css2?family=Lexend:wght@300;400;500;600&family=Poppins:wght@400;500;600&display=swap" rel="stylesheet">
<style>
:root{
  --gold:#d4a43a;
  --gold-light:#e8c462;
  --gold-dark:#b9862a;
  --cream:#fbf4e8;
  --cream-2:#f7eee0;
  --ink:#1c1c1c;
  --text:#3a3a3a;
  --white:#ffffff;
}
*{box-sizing:border-box;margin:0;padding:0}
html,body{width:1200px;height:4713px;overflow:hidden}
body{position:relative;background:var(--white);font-family:"Poppins",sans-serif;color:var(--text)}
.abs{position:absolute}
h1,h2,h3{font-family:"Lexend",sans-serif;font-weight:400;color:var(--ink)}
.btn{position:absolute;display:flex;align-items:center;justify-content:center;font-family:"Poppins",sans-serif;font-weight:600;font-size:16px;color:var(--white);background:linear-gradient(90deg,var(--gold-light),var(--gold));text-decoration:none}
.btn.dark{background:var(--ink)}
.section-title{position:absolute;left:0;width:1200px;text-align:center;font-size:36px}
.title-rule{position:absolute;left:570px;width:60px;height:10px;border-top:3px solid var(--gold);border-bottom:2px solid var(--gold-light)}
.brand{display:flex;align-items:center;gap:10px;font-family:"Lexend",sans-serif;font-weight:500;font-size:28px;color:var(--gold);letter-spacing:1px}
.brand-dot{width:38px;height:38px;border-radius:50%;background:var(--gold)}

/* hero */
.hero{position:absolute;left:0;top:0;width:1200px;height:710px;background:linear-gradient(90deg,var(--cream) 0%,#f8ecdc 45%,#f3e4d2 100%);overflow:hidden}
.hero-photo{position:absolute;left:600px;top:0;width:600px;height:710px;background:radial-gradient(ellipse at 60% 40%,#e9b79d 0%,#d99a7e 30%,#c9845f 55%,#efe3d3 85%)}
.nav{position:absolute;left:100px;top:22px;width:1000px;height:44px;display:flex;align-items:center}
.nav-links{display:flex;gap:0;margin-left:46px;font-size:14px;font-weight:500;color:var(--ink)}
.nav-links span{padding:0 17px;border-right:1px solid #cfc3b0}
.nav-links span:last-child{border-right:none}
.hero h1{position:absolute;left:102px;top:182px;font-size:41px;line-height:52px;font-weight:400;letter-spacing:1px}
.hero h1 .gold{color:var(--gold)}
.hero-sub{position:absolute;left:104px;top:352px;width:400px;font-size:13.5px;line-height:20px;color:var(--ink)}
.shipping-note{position:absolute;left:112px;top:476px;font-size:13.5px;color:var(--ink);display:flex;gap:8px;align-items:center}
.product-box{position:absolute;background:linear-gradient(135deg,#1a1a1a 0%,#1a1a1a 45%,var(--gold) 46%,#1a1a1a 52%);border-radius:4px;box-shadow:12px 14px 24px rgba(0,0,0,.25)}
.hero-wave{position:absolute;left:0;top:600px}

/* benefits */
.card{position:absolute;width:314px;height:208px;border:2px solid var(--gold-light);border-radius:0 60px 0 0;text-align:center;padding:68px 30px 0}
.card h3{font-family:"Poppins",sans-serif;font-weight:600;font-size:16px;color:var(--ink);margin-bottom:8px}
.card p{font-size:14.5px;line-height:22px;color:var(--ink)}
.icon-badge{position:absolute;width:90px;height:90px;border-radius:50%;background:linear-gradient(135deg,var(--gold-light),var(--gold-dark));display:flex;align-items:center;justify-content:center;box-shadow:0 0 0 6px #fbf1da}

/* future band */
.band{position:absolute;left:0;top:1496px;width:1200px;height:700px;background:linear-gradient(100deg,#e7c155 0%,#d9a840 50%,#c8882c 100%);overflow:hidden}
.band h2{position:absolute;left:636px;top:120px;font-size:36px;line-height:45px;color:var(--white)}
.band p{position:absolute;left:640px;top:248px;width:470px;font-size:15.5px;line-height:28px;color:var(--white)}

/* steps */
.step{position:absolute;width:220px;height:220px;border-radius:50%;background:var(--ink);color:var(--white);text-align:center;display:flex;flex-direction:column;align-items:center;justify-content:center;padding:0 28px}
.step strong{font-family:"Lexend",sans-serif;font-weight:400;font-size:17px;margin:10px 0 4px}
.step span{font-size:12px;line-height:18px}
.step-ring{position:absolute;width:250px;height:250px;border-radius:50%;border:2px solid var(--gold-light)}

/* reviews */
.reviews{position:absolute;left:0;top:2775px;width:1200px;height:526px;background:var(--cream)}
.review{position:absolute;width:418px;height:212px;background:var(--white);border:1px solid #e6ddd0;text-align:center;padding-top:58px}
.stars{color:var(--gold);letter-spacing:3px;font-size:18px}
.review p{font-size:15px;line-height:22px;color:var(--text);margin:10px 40px 14px}
.review .who{font-weight:500;font-size:16px;color:var(--ink)}
.quote-badge{position:absolute;width:54px;height:54px;border-radius:50%;background:var(--gold);color:var(--white);font-family:"Lexend",sans-serif;font-size:38px;line-height:64px;text-align:center}

/* faq */
.faq{position:absolute;left:159px;width:888px;border:2px solid #e9d9b4;background:var(--white);padding:0 32px}
.faq h4{font-family:"Poppins",sans-serif;font-weight:600;font-size:17px;color:var(--ink)}
.faq p{font-size:13.5px;color:var(--text);margin-top:10px}
.faq-toggle{position:absolute;right:14px;width:26px;height:26px;border-radius:50%;background:var(--gold-light);color:var(--white);font-size:20px;line-height:24px;text-align:center}

/* cta + footer */
.footer{position:absolute;left:0;top:4340px;width:1200px;height:373px;background:var(--ink)}
.cta-card{position:absolute;left:128px;top:4006px;width:960px;height:452px;border-radius:110px 0 60px 0;background:linear-gradient(100deg,#e7c155,#d6a33a 60%,#c58a2d)}
.cta-card h2{position:absolute;left:475px;top:110px;font-size:31px;line-height:36px;color:var(--white)}
.foot-links{position:absolute;top:4586px;font-size:14px;color:var(--white);display:flex;gap:36px}
.copyright{position:absolute;left:184px;top:4656px;font-size:12px;color:#b9b2a6}
.social{position:absolute;top:4648px;width:36px;height:36px;border-radius:50%;background:var(--gold)}
</style>
</head>
<body>

<!-- HERO -->
<section class="hero">
  <div class="hero-photo" role="img" aria-label="Foto van een vrouw die ruikt aan een zachte, vers gewassen roze handdoek"></div>
  <nav class="nav">
    <div class="brand"><span class="brand-dot"></span>PLOOIFRIS</div>
    <div class="nav-links"><span>Voordelen</span><span>Product</span><span>Hoe het werkt</span><span>Beoordelingen</span><span>FAQ</span></div>
    <a class="btn" style="left:854px;top:0;width:124px;height:38px;font-size:14px;font-weight:500">Probeer nu</a>
  </nav>
  <h1><span class="gold">ERVAAR LUXE EN</span><br>DUURZAAMHEID IN<br>ELKE WASBEURT</h1>
  <p class="hero-sub">Ontdek de premium wasstrips van Plooifris – waar verfijning en ecologisch bewustzijn samenkomen</p>
  <a class="btn" style="left:107px;top:412px;width:164px;height:42px">Probeer Nu&nbsp;›</a>
  <div class="shipping-note">
    <svg width="20" height="14" viewBox="0 0 20 14"><rect x="1" y="2" width="11" height="8" fill="none" stroke="#1c1c1c" stroke-width="1.5"/><path d="M12 5h4l3 3v2h-7z" fill="none" stroke="#1c1c1c" stroke-width="1.5"/><circle cx="5" cy="11.5" r="1.8" fill="#1c1c1c"/><circle cx="15" cy="11.5" r="1.8" fill="#1c1c1c"/></svg>
    Altijd Gratis Verzending!
  </div>
  <svg class="hero-wave" width="1200" height="110" viewBox="0 0 1200 110">
    <path d="M0 95 C300 20 620 30 820 70 C980 100 1100 90 1200 70 L1200 110 L0 110Z" fill="#ffffff"/>
    <path d="M0 95 C300 20 620 30 820 70 C980 100 1100 90 1200 70" fill="none" stroke="#d4a43a" stroke-width="5"/>
  </svg>
  <div class="product-box" style="left:466px;top:393px;width:202px;height:302px" role="img" aria-label="Verpakking Plooifris wasstrips, zwart met goud"></div>
</section>

<!-- BENEFITS -->
<h2 class="section-title" style="top:780px;font-size:30px">Waarom Kiezen Voor Plooifris Wasstrips?</h2>
<div class="title-rule" style="top:830px"></div>

<div class="card" style="left:113px;top:920px"><h3>Milieuvriendelijk</h3><p>100% biologisch afbreekbaar en plasticvrij.</p></div>
<div class="card" style="left:454px;top:920px"><h3>Geschikt voor Alle Stoffen</h3><p>Veilig voor fijne was, wit, kleur en zwart.</p></div>
<div class="card" style="left:794px;top:920px;padding-top:60px"><h3>Compact en Gebruiksvriendelijk</h3><p>Geen gedoe met zware flessen – scheur, voeg toe en geniet.</p></div>
<div class="card" style="left:116px;top:1186px"><h3>Langdurige Geur</h3><p>Een heerlijke frisse geur die dagenlang blijft hangen.</p></div>
<div class="card" style="left:457px;top:1186px"><h3>Hypoallergeen</h3><p>Perfect voor de gevoelige huid en babykleding.</p></div>
<div class="card" style="left:797px;top:1186px"><h3>Altijd Gratis Verzending</h3><p>Geen minimale bestelhoeveelheid vereist.</p></div>

<div class="icon-badge" style="left:225px;top:878px"><svg width="40" height="40" viewBox="0 0 40 40"><path d="M20 6c8 4 10 14 2 24-8-6-10-16-2-24z" fill="none" stroke="#fff" stroke-width="2"/><path d="M20 8v22" stroke="#fff" stroke-width="2"/></svg></div>
<div class="icon-badge" style="left:566px;top:878px"><svg width="40" height="40" viewBox="0 0 40 40"><rect x="9" y="12" width="22" height="20" rx="2" fill="none" stroke="#fff" stroke-width="2"/><path d="M14 12v-4h12v4" fill="none" stroke="#fff" stroke-width="2"/></svg></div>
<div class="icon-badge" style="left:906px;top:878px"><svg width="40" height="40" viewBox="0 0 40 40"><path d="M20 6c6 8 9 13 9 18a9 9 0 0 1-18 0c0-5 3-10 9-18z" fill="none" stroke="#fff" stroke-width="2"/></svg></div>
<div class="icon-badge" style="left:228px;top:1144px"><svg width="40" height="40" viewBox="0 0 40 40"><path d="M12 32c-4-6 6-10 2-18M20 32c-4-6 6-10 2-18M28 32c-4-6 6-10 2-18" fill="none" stroke="#fff" stroke-width="2"/></svg></div>
<div class="icon-badge" style="left:569px;top:1144px"><svg width="40" height="40" viewBox="0 0 40 40"><path d="M8 12l8-4h8l8 4-3 7-3-1v14H14V18l-3 1z" fill="none" stroke="#fff" stroke-width="2"/></svg></div>
<div class="icon-badge" style="left:909px;top:1144px"><svg width="44" height="40" viewBox="0 0 44 40"><rect x="4" y="10" width="22" height="16" fill="none" stroke="#fff" stroke-width="2"/><path d="M26 15h8l5 5v6H26z" fill="none" stroke="#fff" stroke-width="2"/><circle cx="12" cy="29" r="3" fill="#fff"/><circle cx="33" cy="29" r="3" fill="#fff"/></svg></div>

<!-- FUTURE BAND -->
<section class="band">
  <svg class="abs" style="left:0;top:0" width="1200" height="700" viewBox="0 0 1200 700"><path d="M0 690 C300 600 700 600 1200 640 L1200 700 L0 700Z" fill="#ffffff"/></svg>
  <div class="abs" style="left:100px;top:56px;width:464px;height:464px;border-radius:50%;border:10px solid #f1d486;border-right-color:transparent;border-top-color:transparent;transform:rotate(45deg)"></div>
  <div class="abs" style="left:124px;top:75px;width:436px;height:436px;border-radius:50%;background:#111"></div>
  <div class="abs" style="left:138px;top:89px;width:408px;height:408px;border-radius:50%;background:radial-gradient(circle at 40% 55%,#ffffff 0%,#e8e6e2 40%,#c9c4bb 75%,#8d8a7a 100%)" role="img" aria-label="Foto van een witte wasmachine met een plant op de achtergrond"></div>
  <div class="product-box" style="left:396px;top:330px;width:148px;height:236px" role="img" aria-label="Verpakking Plooifris wasstrips"></div>
  <h2>De Toekomst van<br>Wassen Is Hier</h2>
  <div class="abs" style="left:639px;top:234px;width:58px;border-top:3px solid #fff"></div>
  <p>Onze Plooifris Wasstrips combineren innovatie met duurzaamheid. Met slechts één strip per wasbeurt geniet je van een schone en heerlijk geurende was, zonder het milieu te belasten. Geen plastic flessen, geen verspilling – alleen pure waskracht in een handige strip.</p>
  <a class="btn dark" style="left:640px;top:414px;width:157px;height:44px;font-size:15px">Probeer Nu&nbsp;›</a>
</section>

<!-- STEPS -->
<h2 class="section-title" style="top:2250px">Zo Gebruik Je Wasstrips</h2>
<div class="title-rule" style="top:2305px"></div>

<div class="step-ring" style="left:90px;top:2358px"></div>
<div class="step-ring" style="left:347px;top:2358px"></div>
<div class="step-ring" style="left:606px;top:2358px"></div>
<div class="step-ring" style="left:867px;top:2358px"></div>
<div class="step" style="left:108px;top:2374px">
  <svg width="58" height="50" viewBox="0 0 58 50"><path d="M6 10l12-6h12l12 6-5 10-5-2v26H16V18l-5 2z" fill="#e0b44a"/><rect x="44" y="14" width="10" height="14" fill="none" stroke="#fff" stroke-width="1.5" transform="rotate(20 49 21)"/></svg>
  <strong>Step 1</strong><span>Scheur een wasstrip af.</span></div>
<div class="step" style="left:364px;top:2374px">
  <svg width="50" height="54" viewBox="0 0 50 54"><rect x="8" y="14" width="34" height="36" rx="3" fill="none" stroke="#e0b44a" stroke-width="2.5"/><circle cx="25" cy="34" r="9" fill="none" stroke="#e0b44a" stroke-width="2.5"/><path d="M14 14V6h22v8" fill="none" stroke="#e0b44a" stroke-width="2.5"/></svg>
  <strong>Step 2</strong><span>Plaats de strip direct in de trommel, samen met je wasgoed.</span></div>
<div class="step" style="left:623px;top:2374px">
  <svg width="46" height="54" viewBox="0 0 46 54"><rect x="4" y="2" width="38" height="50" rx="3" fill="#e0b44a"/><circle cx="23" cy="30" r="12" fill="#1c1c1c"/><circle cx="23" cy="30" r="7" fill="#e0b44a"/></svg>
  <strong>Step 3</strong><span>Start de wasmachine en laat de wasstrip zijn werk doen.</span></div>
<div class="step" style="left:885px;top:2374px">
  <svg width="58" height="50" viewBox="0 0 58 50"><path d="M8 10l12-6h12l12 6-5 10-5-2v26H18V18l-5 2z" fill="#e0b44a"/><path d="M26 24h6M29 21v6" stroke="#fff" stroke-width="1.5"/></svg>
  <strong>Step 4</strong><span>Geniet van perfect schone en fris ruikende kleding!</span></div>

<a class="btn" style="left:476px;top:2660px;width:248px;height:48px;font-size:15px">Shop Nu – Vanaf €14,95</a>

<!-- REVIEWS -->
<section class="reviews">
  <h2 class="section-title" style="top:54px">Wat Onze Klanten Zeggen</h2>
  <div class="title-rule" style="top:110px"></div>
  <svg class="abs" style="left:102px;top:268px" width="28" height="50" viewBox="0 0 28 50"><path d="M24 2L4 25l20 23" fill="none" stroke="#d4a43a" stroke-width="3"/></svg>
  <svg class="abs" style="left:1084px;top:268px" width="28" height="50" viewBox="0 0 28 50"><path d="M4 2l20 23L4 48" fill="none" stroke="#d4a43a" stroke-width="3"/></svg>
  <div class="abs" style="left:170px;top:193px;width:60px;height:60px;border-left:6px solid var(--gold);border-top:6px solid var(--gold)"></div>
  <div class="abs" style="left:986px;top:360px;width:64px;height:60px;border-right:6px solid var(--gold);border-bottom:6px solid var(--gold)"></div>
  <div class="review" style="left:177px;top:201px"><p class="stars">★★★★★</p><p>"Sinds ik Plooifris gebruik, voelt mijn was frisser en luxueuzer aan dan ooit."</p><span class="who">– Lotte</span></div>
  <div class="review" style="left:627px;top:201px"><p class="stars">★★★★★</p><p>"Eindelijk een milieuvriendelijk product dat echt werkt en heerlijk ruikt."</p><span class="who">– Daan</span></div>
  <div class="quote-badge" style="left:359px;top:177px">“</div>
  <div class="quote-badge" style="left:809px;top:177px">“</div>
</section>

<!-- FAQ -->
<h2 class="section-title" style="top:3430px">Heb Je Nog Vragen?</h2>
<div class="title-rule" style="top:3485px"></div>

<div class="faq" style="top:3528px;height:140px;padding-top:36px"><h4>Zijn de wasstrips geschikt voor mensen met een gevoelige huid?</h4><p>Ja, onze wasstrips zijn hypoallergeen en dermatologisch getest, waardoor ze veilig zijn voor de gevoelige huid.</p><span class="faq-toggle" style="top:32px">–</span></div>
<div class="faq" style="top:3678px;height:60px;padding-top:18px"><h4>Hoeveel wasbeurten bevat één verpakking?</h4><span class="faq-toggle" style="top:15px">+</span></div>
<div class="faq" style="top:3749px;height:62px;padding-top:18px"><h4>Werken de strips bij lage temperaturen?</h4><span class="faq-toggle" style="top:16px">+</span></div>

<a class="btn" style="left:404px;top:3852px;width:392px;height:57px;font-size:16px">Bekijk Onze FAQ Voor Meer Antwoorden</a>

<!-- CTA + FOOTER -->
<footer class="footer"></footer>
<div class="abs" style="left:118px;top:3996px;width:980px;height:472px;border-radius:116px 0 66px 0;border:2px solid #f0dfb4;border-bottom:none"></div>
<section class="cta-card">
  <div class="product-box" style="left:140px;top:62px;width:200px;height:326px" role="img" aria-label="Verpakking Plooifris wasstrips"></div>
  <h2>Start Vandaag Met<br>Milieuvriendelijk Wassen<br>Geen Plastic, Geen Gedoe.<br><span style="font-size:24px">Alleen Fris Wassen.</span></h2>
  <div class="abs" style="left:476px;top:270px;width:64px;border-top:3px solid #fff"></div>
  <a class="btn dark" style="left:476px;top:296px;width:306px;height:52px;font-size:16px">Bestel Nu – Maak Het Verschil!</a>
</section>

<div class="abs" style="left:0;top:4484px;width:1200px;display:flex;flex-direction:column;align-items:center;gap:10px">
  <span class="brand-dot" style="width:56px;height:56px"></span>
  <span class="brand" style="font-size:24px">PLOOIFRIS</span>
</div>
<div class="foot-links" style="left:188px"><span>Voordelen</span><span>Product</span><span>Hoe het werkt</span></div>
<div class="foot-links" style="left:728px"><span>Beoordelingen</span><span>FAQ</span><span>Probeer nu</span></div>
<p class="copyright">Copyright © 2024 Wasstrips. Alle rechten voorbehouden.</p>
<span class="social" style="left:838px" aria-label="Sociale media"></span>
<span class="social" style="left:880px" aria-label="Sociale media"></span>
<span class="social" style="left:922px" aria-label="Sociale media"></span>
<span class="social" style="left:964px" aria-label="Sociale media"></span>

</body>
</html>
```